Book Cover for College Series

We need an e-book cover design for a collection of poetry entitled, "Chalk Lanterns Vol. 1: The Heartland." Although the price is set to $200, whomever I select for this project will be used for the next three volumes of the series in the future. So be sure to have contact information ready if selected.
If selected, we can be reached at BrightQuillPress@mailnest.example
Be sure to check out the Look and Feel Slider. We would like it to come across as serious and professional, yet very personable and modern.
Target Market(s)
Target market is both current college students as well as former college students (University alums). However, on some level it is marketed towards anyone associated with universities, including professors, as well as poetry readers. Which is why, although personable, We need the look to have a serious feel to it as well.
Industry/Entity Type
College
Requirements
Must have
- The title of the book: "Chalk Lanterns: Vol 1. The Heartland"
- Be sure to have the author's name: Benedict Marlow Tesh
Nice to have
- - Nice to have a design that somehow gives off the feeling of nostalgia.
Optional: Underneath the title, include "A collection of poetry celebrating the top universities of the Midwest."
- Only include the following if it does not get in the way of the feel/look of the cover: Have the initials: B.M.T. on the left-hand corner. An example of how this should appear is in the photo attached However, it does not necessarily need to be this big.

```html
<!DOCTYPE html>
<html lang="en">
<head>
<meta charset="utf-8">
<title>Chalk Lanterns Vol. 1: The Heartland</title>
<link href="https://fonts.googleapis.com/css2?family=Cinzel:wght@400;500&display=swap" rel="stylesheet">
<style>
  :root {
    --ink-light: #f7f1e6;
    --band-gold: #e0a42b;
    --sepia-deep: #1a0f06;
    --sepia-mid: #6b4a22;
    --sepia-warm: #b98c4f;
    --sepia-glow: #f3dfb0;
  }
  html, body {
    margin: 0;
    padding: 0;
    width: 750px;
    height: 1200px;
    overflow: hidden;
    background: var(--sepia-deep);
  }
  .cover {
    position: relative;
    width: 750px;
    height: 1200px;
    overflow: hidden;
    font-family: "Cinzel", "Times New Roman", serif;
    color: var(--ink-light);
  }
  .cover-photo {
    position: absolute;
    inset: 0;
    background:
      radial-gradient(ellipse 160px 240px at 410px 560px, var(--sepia-glow) 0%, rgba(243,223,176,0.55) 35%, rgba(243,223,176,0) 100%),
      radial-gradient(ellipse 420px 520px at 400px 520px, rgba(185,140,79,0.85) 0%, rgba(107,74,34,0.6) 55%, rgba(26,15,6,0) 100%),
      linear-gradient(180deg, #3a2710 0%, var(--sepia-mid) 30%, #5a3d1c 55%, #22160a 75%, #0b0703 100%);
  }
  .series-title {
    position: absolute;
    top: 60px;
    left: 0;
    width: 750px;
    margin: 0;
    text-align: center;
    font-weight: 400;
    line-height: 1;
    text-shadow: 0 2px 6px rgba(0,0,0,0.45);
  }
  .series-title .title-main {
    display: block;
    font-size: 62px;
    letter-spacing: 1px;
  }
  .series-title .title-volume {
    display: block;
    margin-top: 22px;
    font-size: 45px;
    letter-spacing: 0;
  }
  .subtitle-band {
    position: absolute;
    top: 282px;
    left: 0;
    width: 750px;
    height: 100px;
    background: var(--band-gold);
    display: flex;
    align-items: center;
    justify-content: center;
  }
  .subtitle-band p {
    margin: 0;
    text-align: center;
    font-size: 26px;
    line-height: 1.25;
    color: var(--ink-light);
    font-variant: small-caps;
    text-transform: none;
  }
  .author-name {
    position: absolute;
    bottom: 68px;
    left: 0;
    width: 750px;
    margin: 0;
    text-align: center;
    font-size: 40px;
    font-weight: 400;
    letter-spacing: 0.5px;
    text-shadow: 0 2px 4px rgba(0,0,0,0.5);
  }
</style>
</head>
<body>
  <main class="cover">
    <div class="cover-photo" role="img" aria-label="Sepia photograph of two students climbing a dim university staircase toward a bright doorway under a hanging lamp"></div>

    <h1 class="series-title">
      <span class="title-main">CHALK LANTERNS</span>
      <span class="title-volume">VOL. 1: THE HEARTLAND</span>
    </h1>

    <div class="subtitle-band">
      <p>A Collection of Poetry Celebrating<br>The Top Universities of the Midwest</p>
    </div>

    <p class="author-name">BENEDICT MARLOW TESH</p>
  </main>
</body>
</html>
```